Electrical contractor in San Diego county since 1988

Provide a company name/ logo for business cards and forms. Newer and more modern old card is attached. Color preference is black and orange. Simple and streamlined nothing too busy. I have also attached a card that represents the simplicity of what we are looking for.

Contractor

```html
<!DOCTYPE html>
<html lang="en">
<head>
<meta charset="utf-8">
<title>Coastline Wiring Co – Business Card</title>
<link rel="stylesheet" href="https://fonts.googleapis.com/css2?family=Didact+Gothic&family=Quicksand:wght@500;700&display=swap">
<style>
  :root {
    --page-bg: #e4e4e2;
    --card-orange: #e0932a;
    --band-black: #131313;
    --brand-yellow: #f3c64a;
    --ink: #111111;
  }
  * { box-sizing: border-box; margin: 0; padding: 0; }
  html, body {
    width: 1200px; height: 1200px; overflow: hidden;
    background: var(--page-bg);
  }
  .stage {
    width: 1200px; height: 1200px;
    display: flex; align-items: center; justify-content: center;
  }
  .business-card {
    position: relative;
    width: 1000px; height: 571px;
    background: var(--card-orange);
    overflow: hidden;
    box-shadow: 0 10px 30px rgba(0,0,0,0.18);
    font-family: "Didact Gothic", sans-serif;
    color: var(--ink);
  }
  .card-band {
    position: absolute; inset: 0;
    width: 1000px; height: 571px;
  }
  .license {
    position: absolute; left: 172px; top: 48px;
    font-size: 24px; color: var(--brand-yellow);
    letter-spacing: 1px;
  }
  .company-name {
    position: absolute; left: 168px; top: 86px;
    font-size: 56px; font-weight: 400; color: var(--brand-yellow);
    letter-spacing: 1px; white-space: nowrap;
  }
  .tagline {
    position: absolute; left: 172px; top: 166px;
    font-size: 25px; color: var(--brand-yellow);
    letter-spacing: 1px;
  }
  .person {
    position: absolute; left: 48px; top: 290px;
    font-family: "Quicksand", sans-serif;
  }
  .person-name {
    font-size: 32px; font-weight: 700; letter-spacing: 3px;
  }
  .person-title {
    font-size: 21px; font-weight: 700; margin-top: 2px;
  }
  .contact {
    position: absolute; left: 540px; top: 300px;
    font-size: 20px; line-height: 1.35;
  }
  .contact-row { display: flex; margin-bottom: 14px; }
  .contact-label {
    font-family: "Quicksand", sans-serif; font-weight: 700;
    letter-spacing: 1.5px; white-space: nowrap;
  }
  .contact-label.plain { font-weight: 500; }
  .contact-sep { margin: 0 10px; }
  .contact-sep.wide { margin: 0 10px 0 60px; }
  .contact-value { font-size: 18px; letter-spacing: 1px; }
</style>
</head>
<body>
<main class="stage">
  <article class="business-card">
    <svg class="card-band" viewBox="0 0 1000 571" aria-hidden="true">
      <polygon points="230,0 1000,0 1000,222 0,222 0,70" fill="var(--band-black)"/>
      <rect x="0" y="236" width="1000" height="3" fill="var(--band-black)"/>
    </svg>

    <p class="license">Lic - 472816</p>
    <h1 class="company-name">Coastline Wiring Co</h1>
    <p class="tagline">Commercial - New &amp; Remodel</p>

    <div class="person">
      <p class="person-name">DANIEL MARSH</p>
      <p class="person-title">President</p>
    </div>

    <div class="contact">
      <div class="contact-row">
        <span class="contact-label">ADDRESS</span>
        <span class="contact-sep">-</span>
        <span class="contact-value">P.O. Box 2417 Alpine,<br>CA 91901-0417</span>
      </div>
      <div class="contact-row">
        <span class="contact-label plain">PHONE</span>
        <span class="contact-sep">-</span>
        <span class="contact-value">(619) 555-0142</span>
      </div>
      <div class="contact-row">
        <span class="contact-label plain">Fax</span>
        <span class="contact-sep wide">-</span>
        <span class="contact-value">555-0187</span>
      </div>
    </div>
  </article>
</main>
</body>
</html>
```